I need this done FAST!
Business Cards and Stationary for new home construction company - Construction
Simple
Gerald Finch
Owner
4816 Marlow Ct #306142 Houston, TX 77391
Gerald@thequillstoneframeworks.com
www.thequillstoneframeworks.com
I would like this business card to be minimal in its design. I just want it to be a way of saying ... Hi, call me directly. It does not need to be an advertisement. I need the vector files of this please
Front should be the logo only, and the back should be this information: Design~Build Firm Gerald Finch, Owner Phone Email Web address

```html
<!DOCTYPE html>
<html lang="en">
<head>
<meta charset="utf-8">
<title>Quillstone Frameworks – Business Card</title>
<link rel="stylesheet" href="https://fonts.googleapis.com/css2?family=Montserrat:wght@500;600;700;800&display=swap">
<style>
  :root {
    --backdrop: #9a9b9d;
    --card-white: #ffffff;
    --brand-red: #d7141a;
    --brand-red-deep: #a50d12;
    --wave-grey: #c9cacc;
    --wave-grey-light: #e4e5e6;
    --tagline-grey: #6f7073;
    --ink-light: #ffffff;
  }
  * { box-sizing: border-box; margin: 0; padding: 0; }
  html, body { width: 1200px; height: 818px; overflow: hidden; }
  body {
    background: var(--backdrop);
    font-family: "Montserrat", sans-serif;
    position: relative;
  }
  .card {
    position: absolute;
    width: 525px;
    height: 300px;
    border-radius: 16px;
    overflow: hidden;
    background: var(--card-white);
  }
  .card--front { left: 50px; top: 259px; }
  .card--back  { left: 625px; top: 259px; }

  .brand {
    display: flex;
    align-items: center;
    gap: 10px;
    color: var(--brand-red);
    font-weight: 800;
    text-transform: uppercase;
    letter-spacing: 0.5px;
    white-space: nowrap;
  }
  .brand__mark {
    width: 18px; height: 18px;
    background: var(--brand-red);
  }
  .card--front .brand {
    position: absolute;
    inset: 0;
    justify-content: center;
    font-size: 26px;
  }

  .back-brand {
    position: absolute;
    left: 30px; top: 42px;
  }
  .back-brand .brand { font-size: 20px; }
  .back-brand .brand__mark { width: 14px; height: 14px; }
  .tagline {
    margin: 5px 0 0 24px;
    color: var(--tagline-grey);
    font-size: 9px;
    font-weight: 600;
    text-transform: uppercase;
    letter-spacing: 2px;
  }

  .back-waves { position: absolute; inset: 0; }

  .holder {
    position: absolute;
    left: 30px; bottom: 60px;
    color: var(--ink-light);
  }
  .holder__name { font-size: 19px; font-weight: 700; text-transform: uppercase; letter-spacing: 0.5px; }
  .holder__title { font-size: 9px; font-weight: 500; text-transform: uppercase; letter-spacing: 1px; margin-top: 3px; }

  .contacts {
    position: absolute;
    right: 22px; bottom: 18px;
    list-style: none;
    color: var(--ink-light);
    font-size: 9px;
    font-weight: 500;
    text-align: right;
  }
  .contacts li {
    display: flex;
    align-items: center;
    justify-content: flex-end;
    gap: 7px;
    line-height: 1.25;
    margin-top: 5px;
  }
  .contacts .address { margin-bottom: 8px; }
  .contacts svg { width: 11px; height: 11px; flex: none; }
</style>
</head>
<body>

<section class="card card--front" aria-label="Card front">
  <div class="brand"><span class="brand__mark"></span>Quillstone Frameworks</div>
</section>

<section class="card card--back" aria-label="Card back">
  <svg class="back-waves" viewBox="0 0 525 300" preserveAspectRatio="none" aria-hidden="true">
    <defs>
      <linearGradient id="redFill" x1="0" y1="0" x2="1" y2="1">
        <stop offset="0" stop-color="#d7141a"/>
        <stop offset="1" stop-color="#a50d12"/>
      </linearGradient>
    </defs>
    <path d="M0 150 C140 150 260 95 525 80 L525 300 L0 300 Z" fill="#e4e5e6"/>
    <path d="M0 165 C160 160 280 112 525 100 L525 300 L0 300 Z" fill="#c9cacc"/>
    <path d="M0 178 C170 172 300 128 525 118 L525 300 L0 300 Z" fill="#ffffff"/>
    <path d="M0 190 C180 184 310 140 525 132 L525 300 L0 300 Z" fill="url(#redFill)"/>
  </svg>

  <div class="back-brand">
    <div class="brand"><span class="brand__mark"></span>Quillstone Frameworks</div>
    <p class="tagline">Design~Build Firm</p>
  </div>

  <div class="holder">
    <p class="holder__name">Gerald Finch</p>
    <p class="holder__title">Owner</p>
  </div>

  <ul class="contacts">
    <li class="address">4816 Marlow Ct #306142<br>Houston, TX 77391</li>
    <li>713 555 0142
      <svg viewBox="0 0 12 12"><path d="M3 1 L5 3.5 L4 5 Q5 7 7 8 L8.5 7 L11 9 L9.5 11 Q4 10.5 1 3 Z" fill="currentColor"/></svg></li>
    <li>713 555 0187
      <svg viewBox="0 0 12 12"><rect x="3" y="1" width="6" height="10" rx="1" fill="none" stroke="currentColor" stroke-width="1.2"/></svg></li>
    <li>713 555 0163
      <svg viewBox="0 0 12 12"><rect x="1" y="3" width="10" height="7" fill="none" stroke="currentColor" stroke-width="1.2"/><rect x="3" y="1" width="6" height="3" fill="currentColor"/></svg></li>
    <li>Gerald@thequillstoneframeworks.com
      <svg viewBox="0 0 12 12"><rect x="1" y="2.5" width="10" height="7" fill="none" stroke="currentColor" stroke-width="1.2"/><path d="M1 2.5 L6 7 L11 2.5" fill="none" stroke="currentColor" stroke-width="1.2"/></svg></li>
    <li>www.thequillstoneframeworks.com
      <svg viewBox="0 0 12 12"><circle cx="6" cy="6" r="5" fill="none" stroke="currentColor" stroke-width="1.2"/><path d="M1 6 H11 M6 1 Q3 6 6 11 Q9 6 6 1" fill="none" stroke="currentColor" stroke-width="1"/></svg></li>
  </ul>
</section>

</body>
</html>
```